MORLO's Coffee Liqueur Shot Arabica

Need a lable for a 500ml bottle of homemade Coffee liqueur.
Name:
MORLO's
Coffee
Shot

Shape: Round, 80mm
Color of the lable should be black and letters in black.
Letters MORLO's min 12mm hight.
Color of the liqueur is dark brown.
Add: 500ml
Add: 38% vol.
Should have a bean on the lable.
Maybe some bullet words on the bottom...
Prefered design see Pic1a with bottle.

Target Market(s)

People that enjoy coffee in shots, in coctails, with ice or on top of icecream or any other dessert

Font styles to use
Serif

Colors

Designer to choose colors to be used in the design.

Requirements
Must have
• See Pic 1a
Nice to have
• See Pic1a (bottle)
Should not have
• Different colors

```html
<!DOCTYPE html>
<html lang="en">
<head>
<meta charset="UTF-8">
<title>MORLO's Coffee Shot – Round Label</title>
<link rel="stylesheet" href="https://fonts.googleapis.com/css2?family=Alfa+Slab+One&family=Zilla+Slab:wght@700&family=Libre+Caslon+Text:wght@400;700&display=swap">
<style>
  :root {
    --paper: #f3f1ea;
    --label: #fbfaf6;
    --label-edge: #e6e3da;
    --ink: #141414;
    --silver: #a3a3a3;
    --silver-dark: #8a8a8a;
    --silver-light: #cfcfcf;
    --bean: #3a3a3a;
  }
  html, body {
    margin: 0;
    padding: 0;
    width: 1200px;
    height: 1200px;
    overflow: hidden;
    background: var(--paper);
  }
  .canvas {
    position: relative;
    width: 1200px;
    height: 1200px;
  }
  .label-frame {
    position: absolute;
    inset: 0;
  }
  .ornament {
    position: absolute;
    border-radius: 50%;
    background: radial-gradient(ellipse at center, var(--silver-light) 0%, rgba(207,207,207,0.35) 60%, rgba(207,207,207,0) 100%);
  }
  .ornament--top { left: 352px; top: 160px; width: 494px; height: 126px; }
  .ornament--bottom { left: 434px; top: 938px; width: 330px; height: 84px; }

  .brand-name,
  .product-name,
  .spec,
  .ribbon-text {
    position: absolute;
    left: 0;
    width: 1200px;
    text-align: center;
    margin: 0;
    line-height: 1;
  }
  .brand-name {
    top: 318px;
    font-family: "Alfa Slab One", serif;
    font-size: 112px;
    color: var(--ink);
    letter-spacing: 1px;
  }
  .product-name {
    top: 498px;
    font-family: "Zilla Slab", serif;
    font-weight: 700;
    font-size: 134px;
    color: var(--ink);
    letter-spacing: 1px;
    transform: scaleX(0.9);
  }
  .spec {
    top: 694px;
    font-family: "Libre Caslon Text", serif;
    font-size: 58px;
    color: var(--silver);
    width: auto;
  }
  .spec--volume { left: 250px; }
  .spec--strength { left: 712px; }
  .spec small { font-size: 44px; }
  .spec-dot {
    position: absolute;
    top: 716px;
    width: 10px;
    height: 10px;
    background: var(--silver);
    transform: rotate(45deg);
  }
  .spec-dot--left { left: 505px; }
  .spec-dot--right { left: 670px; }
  .bean {
    position: absolute;
    left: 553px;
    top: 670px;
    width: 92px;
    height: 104px;
    border-radius: 50%;
    background: radial-gradient(ellipse at 40% 35%, #6a6a6a 0%, var(--bean) 55%, #111 100%);
    transform: rotate(18deg);
  }
  .ribbon-text {
    top: 840px;
    font-family: "Libre Caslon Text", serif;
    font-weight: 700;
    font-size: 58px;
    color: var(--ink);
    letter-spacing: 1px;
  }
</style>
</head>
<body>
<main class="canvas">
  <svg class="label-frame" width="1200" height="1200" viewBox="0 0 1200 1200" aria-hidden="true">
    <circle class="label-disc" cx="600" cy="600" r="512" fill="var(--label)" stroke="var(--label-edge)" stroke-width="3"/>
    <circle class="ring-outer" cx="600" cy="600" r="478" fill="none" stroke="var(--silver)" stroke-width="3"/>
    <circle class="ring-inner" cx="600" cy="600" r="468" fill="none" stroke="var(--silver)" stroke-width="2"/>
    <g class="ribbon" fill="var(--label)" stroke="var(--ink)" stroke-width="4" stroke-linejoin="round">
      <path class="ribbon-tail ribbon-tail--left" d="M258 808 L300 800 L300 900 L268 912 L288 870 Z"/>
      <path class="ribbon-tail ribbon-tail--right" d="M942 808 L900 800 L900 900 L932 912 L912 870 Z"/>
      <path class="ribbon-band" d="M282 810 Q600 770 918 810 L918 912 Q600 872 282 912 Z"/>
    </g>
  </svg>

  <div class="ornament ornament--top" role="img" aria-label="Silver scroll flourish ornament"></div>

  <h1 class="brand-name">MORLO’S</h1>
  <p class="product-name">COFFEE SHOT</p>

  <p class="spec spec--volume">500 <small>ML</small></p>
  <span class="spec-dot spec-dot--left"></span>
  <div class="bean" role="img" aria-label="Engraved coffee bean illustration"></div>
  <span class="spec-dot spec-dot--right"></span>
  <p class="spec spec--strength">38% <small>ALC.</small></p>

  <p class="ribbon-text">ARABICA INTENSE</p>

  <div class="ornament ornament--bottom" role="img" aria-label="Silver scroll flourish ornament"></div>
</main>
</body>
</html>
```